Wordpress Design Project - GlimmerNestHub

Take a look at this website, kivomart.example. We are creating something very similar to this, four pages are required. The name of our website is GlimmerNestHub.example
1) The home page which highlights, app of the day, a carousel which highlights featured apps, and top apps in different categories
2) Single App Page - This page will details the app that is selected, app icon, app description, app ratings, and other information you can find on an app page in the Vortiq bazaar
3) A page that list all the apps in a category, for example if the user select, "100 top apps" the page that will display the list of 100 apps, 10 per page, summary of description, a small icon, screenshot etc for each app
4) Review Page - where we review an app of the day, including screenshots, videos, text reviews etc
I do not have any logo at the moment, use these as nav links; home, my apps, reviews, blog and contact. Thank you.
I will like to see a nice creativity. I am open to a very beautiful color combinations. Thank you
App shoppers, people that are looking for new apps, discounted apps etc
Store

```html
<!DOCTYPE html>
<html lang="en">
<head>
<meta charset="utf-8">
<title>GlimmerNestHub – Home</title>
<link rel="stylesheet" href="https://fonts.googleapis.com/css2?family=Mulish:wght@400;600;700&family=Asap+Condensed:wght@500;600&display=swap">
<style>
:root{
  --navy:#0f2655;
  --blue:#1a5aa6;
  --sky:#d5e8fb;
  --red:#c8102e;
  --orange:#e8630a;
  --tabblue:#3a78c9;
  --text:#7b7b7b;
  --dark:#1b1b1b;
  --star:#f5a300;
  --line:#d6d9de;
}
*{margin:0;padding:0;box-sizing:border-box}
html,body{width:929px;height:1200px;overflow:hidden;background:#fff}
body{position:relative;font-family:"Mulish",sans-serif;color:var(--dark)}
.abs{position:absolute}
.header{left:0;top:0;width:929px;height:112px;background:var(--navy)}
.brand{left:114px;top:18px;font-size:28px;color:#fff;font-weight:400;letter-spacing:.2px}
.userbar{right:95px;top:10px;font-size:11px;color:#fff}
.userbar a{color:#f08a2c;text-decoration:underline}
.userbar .sep{margin:0 5px}
.account{right:95px;top:31px;font-size:9px;color:#6ea2e0}
.account b{color:#f08a2c;font-weight:600;margin-left:8px}
.tabs{left:0;top:84px}
.filterbar{left:0;top:112px;width:929px;height:43px;background:linear-gradient(#e6f1fc,#c7dff7)}
.pill{position:absolute;top:13px;height:18px;display:flex;border:1px solid #b4c8de;border-radius:9px;background:#fff;font-size:9.5px;overflow:hidden}
.pill span{padding:0 7px;line-height:16px;border-right:1px solid #d0dae6;color:#223}
.pill span:last-child{border-right:0}
.pill .on{background:var(--blue);color:#fff;border-radius:9px}
.vsep{position:absolute;top:12px;width:1px;height:20px;background:#aac3dd}
.select{left:376px;top:16px;width:109px;height:14px;border:1px solid #8fa4bb;background:#fff;font-size:8.5px;padding-left:3px;line-height:12px}
.select i{position:absolute;right:0;top:0;width:12px;height:12px;background:#dde6ef;border-left:1px solid #8fa4bb}
.aotd{left:86px;top:155px;width:491px;height:243px;background:linear-gradient(#fbfcfd,#e8ebf0);border:1px solid var(--line)}
.aotd h2{position:absolute;left:22px;top:19px;font-weight:400;font-size:21px;color:var(--blue)}
.ph{position:absolute;border-radius:6px}
.aotd-card{left:292px;top:49px;width:188px;height:170px;border:1px solid #e1e5ea;border-radius:6px;background:linear-gradient(#fff,#f3f5f8)}
.cond{font-family:"Asap Condensed",sans-serif}
.app-name{position:absolute;left:14px;top:8px;font-size:16px;color:var(--blue)}
.free{position:absolute;left:14px;top:30px;font-size:14px;color:#e00;font-weight:600}
.meta{position:absolute;left:14px;top:78px;font-size:10.5px;color:var(--blue);line-height:11px;font-weight:600}
.section-title{font-size:18px;font-weight:400;color:var(--dark)}
.more{left:450px;top:427px;font-size:10.5px;color:var(--blue)}
.app{position:absolute;left:103px;width:460px;height:110px}
.app .thumb{left:0;top:0;width:132px;height:106px;border-radius:7px}
.app h3{position:absolute;left:145px;top:0;font-weight:400;font-size:17.5px;color:var(--blue)}
.app p{position:absolute;left:146px;top:24px;font-size:10px;line-height:15.5px;color:var(--text);width:320px}
.app .stars{position:absolute;left:146px;top:73px}
.app .price{position:absolute;left:146px;top:88px;font-size:14.5px;color:var(--blue)}
.app .price s{margin-right:10px}
.buy{position:absolute;left:227px;top:90px;width:55px;height:17px;background:var(--red);color:#fff;font-size:8.5px;border-radius:3px;text-align:center;line-height:17px}
.divider{left:591px;top:452px;width:1px;height:664px;background:var(--line)}
.side{left:609px;width:220px}
.side h4{font-size:13.5px;font-weight:400;color:var(--dark)}
.side .stat{font-size:10.5px;color:var(--text);line-height:16px;margin-top:10px}
.side .lede{font-size:10px;color:var(--text);line-height:15.5px;margin-top:9px}
.feeds{list-style:none;margin-top:13px}
.feeds li{display:flex;align-items:center;height:23.5px;font-size:10.5px;color:var(--text)}
.feeds svg{margin-right:8px}
.footer{left:0;top:1152px;width:929px;height:48px;background:var(--navy);color:#fff;font-size:10.5px;text-align:center;line-height:48px}
</style>
</head>
<body>
<svg width="0" height="0" style="position:absolute">
  <defs>
    <symbol id="star" viewBox="0 0 20 20"><path d="M10 1l2.7 6 6.5.6-4.9 4.3 1.5 6.4L10 15l-5.8 3.3 1.5-6.4L.8 7.6l6.5-.6z" fill="var(--star)" stroke="#d98900" stroke-width=".8"/></symbol>
    <symbol id="rss" viewBox="0 0 16 16"><rect width="16" height="16" rx="3" fill="#f26a1b"/><circle cx="4.2" cy="11.8" r="1.6" fill="#fff"/><path d="M3 7.5a5.5 5.5 0 0 1 5.5 5.5M3 4a9 9 0 0 1 9 9" stroke="#fff" stroke-width="1.8" fill="none"/></symbol>
    <symbol id="five" viewBox="0 0 72 12"><use href="#star" x="0" width="12" height="12"/><use href="#star" x="15" width="12" height="12"/><use href="#star" x="30" width="12" height="12"/><use href="#star" x="45" width="12" height="12"/><use href="#star" x="60" width="12" height="12"/></symbol>
  </defs>
</svg>

<header class="abs header">
  <div class="abs brand">GlimmerNestHub</div>
  <div class="abs userbar">Welcome, Guest <span class="sep">|</span><a>Login</a><span class="sep">|</span><a>Register</a><span class="sep">|</span><a>Forgot Password</a></div>
  <div class="abs account">My Account: <b>125 Points</b></div>
  <svg class="abs tabs" width="929" height="28" viewBox="0 0 929 28" font-family="Mulish, sans-serif" font-size="11.5" text-anchor="middle">
    <path d="M94 28C104 28 106 2 118 2H188C198 2 200 28 210 28Z" fill="#fff"/>
    <path d="M204 28C214 28 216 2 228 2H298C308 2 310 28 320 28Z" fill="var(--red)"/>
    <path d="M316 28C326 28 328 2 340 2H410C420 2 422 28 432 28Z" fill="var(--orange)"/>
    <path d="M428 28C438 28 440 2 452 2H522C532 2 534 28 544 28Z" fill="var(--tabblue)"/>
    <path d="M520 28C530 28 532 2 544 2H614C624 2 626 28 636 28Z" fill="#fff"/>
    <text x="148" y="19" fill="#1b1b1b">Home</text>
    <text x="258" y="19" fill="#fff">My Apps</text>
    <text x="370" y="19" fill="#fff">Reviews</text>
    <text x="476" y="19" fill="#fff">Blog</text>
    <text x="576" y="19" fill="#1b1b1b">Contact</text>
  </svg>
</header>

<nav class="abs filterbar">
  <div class="pill" style="left:110px"><span class="on">Orbit</span><span>Desk</span></div>
  <div class="vsep" style="left:182px"></div>
  <div class="pill" style="left:198px"><span class="on">All</span><span>Phone</span><span>Tablet</span><span>Universal</span></div>
  <div class="abs select">All Categories<i></i></div>
  <div class="vsep" style="left:491px"></div>
  <div class="pill" style="left:503px"><span class="on">All</span><span>Popular</span></div>
  <div class="vsep" style="left:592px"></div>
  <div class="pill" style="left:605px"><span class="on">All</span><span>Updates</span><span>New</span><span>Price Drops</span></div>
</nav>

<section class="abs aotd">
  <h2>APP OF THE DAY</h2>
  <div class="ph" role="img" aria-label="Racing game artwork with a yellow sports car" style="left:18px;top:52px;width:266px;height:168px;background:linear-gradient(135deg,#1c1c1c 0%,#e2b400 40%,#f3d23a 55%,#3a3a3a 80%,#0c0c0c 100%)"></div>
  <div class="abs aotd-card">
    <div class="app-name cond">Turbo Lane HD</div>
    <div class="free cond">FREE</div>
    <svg class="abs" style="left:14px;top:50px" width="90" height="20"><use href="#star" x="0" width="20" height="20"/><use href="#star" x="23" width="20" height="20"/><use href="#star" x="46" width="20" height="20"/><use href="#star" x="69" width="20" height="20"/></svg>
    <div class="meta cond">Action / Racing<br>Developer: Brightpine Studio</div>
    <svg class="abs" style="left:0;top:120px" width="186" height="36">
      <path d="M14 12l-5 6 5 6" stroke="#111" stroke-width="2.4" fill="none"/>
      <path d="M158 12l5 6-5 6" stroke="#111" stroke-width="2.4" fill="none"/>
    </svg>
    <div class="ph" role="img" aria-label="Red race car screenshot" style="left:24px;top:115px;width:29px;height:45px;border-radius:2px;background:linear-gradient(#cfd6dc,#b8222a)"></div>
    <div class="ph" role="img" aria-label="White car screenshot" style="left:71px;top:115px;width:29px;height:45px;border-radius:2px;background:linear-gradient(#6a6f5a,#d9dcd8)"></div>
    <div class="ph" role="img" aria-label="Green car screenshot" style="left:118px;top:115px;width:29px;height:45px;border-radius:2px;background:linear-gradient(#d8dee4,#4f9a3a)"></div>
  </div>
</section>

<div class="ph" role="img" aria-label="Promotional photo of a station platform" style="left:588px;top:164px;width:246px;height:111px;border-radius:0;background:linear-gradient(120deg,#4a4a48,#9c9d98 50%,#cfd0cc)"></div>
<div class="ph" role="img" aria-label="Promotional photo of a smartphone on dark panels" style="left:588px;top:286px;width:245px;height:111px;border-radius:0;background:linear-gradient(90deg,#2b2b2b,#4a4a4a 50%,#2a2a2a)"></div>
<svg class="abs" style="left:648px;top:316px" width="60" height="16"><path d="M0 0H52L58 8 52 16H0Z" fill="#f08a1a"/><text x="8" y="12" font-family="Mulish, sans-serif" font-size="9.5" font-weight="700" fill="#fff">18% OFF</text></svg>

<h2 class="abs section-title" style="left:105px;top:422px">Featured Applications</h2>
<div class="abs more">» &nbsp;View More Applications</div>

<article class="app" style="top:474px">
  <div class="ph thumb" role="img" aria-label="Ancient amphitheatre at dusk" style="background:linear-gradient(135deg,#2a4fd0,#c78a3c 50%,#6b4a2a)"></div>
  <h3>Nova Home Theme Stellar S3</h3>
  <p>Lorem Ipsum is simply dummy text of the printing and typesetting industry. Lorem Ipsum has been the industry's standard dummy text ever since the 1500s, when an unknown printer took a galley</p>
  <svg class="stars" width="72" height="12"><use href="#five"/></svg>
  <div class="price"><s>$.45</s>$.30</div><div class="buy">Buy Now</div>
</article>
<article class="app" style="top:608px">
  <div class="ph thumb" role="img" aria-label="Cricket batsman illustration" style="background:linear-gradient(135deg,#2a2a2a,#1b1b1b 60%,#b32020)"></div>
  <h3>Boundary Bash Cricket Cup</h3>
  <p>Lorem Ipsum is simply dummy text of the printing and typesetting industry. Lorem Ipsum has been the industry's standard dummy text ever since the 1500s, when an unknown printer took a galley</p>
  <svg class="stars" width="72" height="12"><use href="#five"/></svg>
  <div class="price"><s>$.45</s>$.30</div><div class="buy">Buy Now</div>
</article>
<article class="app" style="top:741px">
  <div class="ph thumb" role="img" aria-label="Teal prank app icon artwork" style="background:linear-gradient(135deg,#0d2a30,#2ab2b8 60%,#0f3a40)"></div>
  <h3>Signal Spoof Password Prank</h3>
  <p>Lorem Ipsum is simply dummy text of the printing and typesetting industry. Lorem Ipsum has been the industry's standard dummy text ever since the 1500s, when an unknown printer took a galley</p>
  <svg class="stars" width="72" height="12"><use href="#five"/></svg>
  <div class="price"><s>$.45</s>$.30</div><div class="buy">Buy Now</div>
</article>
<article class="app" style="top:876px">
  <div class="ph thumb" role="img" aria-label="Basketball game artwork" style="background:radial-gradient(circle at 45% 35%,#e8883a,#b14d12 55%,#5a5a5a)"></div>
  <h3>Hoop Toss Shoot</h3>
  <p>Lorem Ipsum is simply dummy text of the printing and typesetting industry. Lorem Ipsum has been the industry's standard dummy text ever since the 1500s, when an unknown printer took a galley</p>
  <svg class="stars" width="72" height="12"><use href="#five"/></svg>
  <div class="price"><s>$.45</s>$.30</div><div class="buy">Buy Now</div>
</article>
<article class="app" style="top:1014px">
  <div class="ph thumb" role="img" aria-label="Flip clock launcher over a meadow" style="background:linear-gradient(#c8861a,#e8b83a 45%,#6a8a2a)"></div>
  <h3>Flip Clock Home Launcher</h3>
  <p>Lorem Ipsum is simply dummy text of the printing and typesetting industry. Lorem Ipsum has been the industry's standard dummy text ever since the 1500s, when an unknown printer took a galley</p>
  <svg class="stars" width="72" height="12"><use href="#five"/></svg>
  <div class="price"><s>$.45</s>$.30</div><div class="buy">Buy Now</div>
</article>

<div class="abs divider"></div>

<aside class="abs side" style="top:425px">
  <h4>Total Apps</h4>
  <div class="stat">Total Apps Approved Today: 1243277<br>Total Available Apps: 154893<br>Total Available phone Apps: 8095876<br>Total Available phone Apps: 8095876</div>
</aside>
<aside class="abs side" style="top:535px">
  <h4>Welcome to GlimmerNestHub</h4>
  <div class="lede">Lorem Ipsum is simply dummy text of the printing and typesetting industry. Lorem Ipsum has been the industry's standard dummy text ever since the 1500s, when an unknown printer took a galley of type and scrambled it to make a type specimen book.</div>
</aside>
<aside class="abs side" style="top:679px">
  <h4>Some Of Our Rss Feeds</h4>
  <ul class="feeds">
    <li><svg width="16" height="16"><use href="#rss"/></svg>Desk Suite Changed</li>
    <li><svg width="16" height="16"><use href="#rss"/></svg>Robo Launcher Starts</li>
    <li><svg width="16" height="16"><use href="#rss"/></svg>Phone 5 is new in Market</li>
    <li><svg width="16" height="16"><use href="#rss"/></svg>Lorem Ipsum Dolor Sit Amet and type</li>
  </ul>
</aside>
<aside class="abs side" style="top:817px">
  <h4>Tablet Rss Feeds</h4>
  <ul class="feeds">
    <li><svg width="16" height="16"><use href="#rss"/></svg>Desk Suite Changed</li>
    <li><svg width="16" height="16"><use href="#rss"/></svg>Robo Launcher Starts</li>
    <li><svg width="16" height="16"><use href="#rss"/></svg>Phone 5 is new in Market</li>
    <li><svg width="16" height="16"><use href="#rss"/></svg>Lorem Ipsum Dolor Sit Amet and type</li>
    <li><svg width="16" height="16"><use href="#rss"/></svg>Robo Launcher Starts</li>
  </ul>
</aside>
<aside class="abs side" style="top:982px">
  <h4>Phone Rss Feeds</h4>
  <ul class="feeds">
    <li><svg width="16" height="16"><use href="#rss"/></svg>Lorem Ipsum Dolor Sit Amet and type</li>
    <li><svg width="16" height="16"><use href="#rss"/></svg>Robo Launcher Starts</li>
    <li><svg width="16" height="16"><use href="#rss"/></svg>Lorem Ipsum Dolor Sit Amet and type</li>
    <li><svg width="16" height="16"><use href="#rss"/></svg>Lorem Ipsum Dolor Sit Amet and type</li>
  </ul>
</aside>

<footer class="abs footer">Copyright©2013 &nbsp;GlimmerNestHub. All Rights Reserved</footer>
</body>
</html>
```